Professional Business Cards

We need a nice looking, profession and modern business card for our new company. Our logo is attatched

Target Market(s)

Young Professionals

Industry/Entity Type

Financial

Contact Information for Business Card

FRONT

Morvane Tally Pty Ltd
Level 22, Halden Court, 48 Wirrapool St
Sydney NSW 2000
ABN : 57 304 918 226

Derek Wallis - Chief Operations Officer
P : 02 7153 2819
M: 0418 395 207
derek@morvanetally,com

BACK

- Cryptocurrency Exchange Services
- Cryptocurrency Mining Operations
- Cryptocurrency Investment Fund Offering

Font styles to use
Sans Serif

Colors
0255a3
9d9d9d

```html
<!DOCTYPE html>
<html lang="en">
<head>
<meta charset="utf-8">
<title>Morvane Tally – Business Card</title>
<link href="https://fonts.googleapis.com/css2?family=Lato:wght@400;700&display=swap" rel="stylesheet">
<style>
  :root {
    --brand-blue: #0255a3;
    --brand-grey: #9d9d9d;
    --card-white: #ffffff;
    --page-bg: #e9e9ec;
  }
  html, body {
    margin: 0;
    padding: 0;
    width: 1200px;
    height: 902px;
    overflow: hidden;
    background: var(--page-bg);
    font-family: "Lato", Arial, sans-serif;
  }
  .canvas {
    position: relative;
    width: 1200px;
    height: 902px;
  }
  .card {
    position: absolute;
    left: 130px;
    top: 183px;
    width: 940px;
    height: 536px;
    border-radius: 22px;
    overflow: hidden;
    background: var(--card-white);
    box-shadow: 0 6px 24px rgba(0,0,0,0.12);
  }
  .card-shapes {
    position: absolute;
    inset: 0;
  }
  .shape-blue { fill: var(--brand-blue); }
  .shape-grey { fill: var(--brand-grey); }

  .details {
    position: absolute;
    left: 43px;
    top: 58px;
    color: var(--card-white);
  }
  .person-name {
    margin: 0;
    font-size: 30px;
    font-weight: 700;
    line-height: 34px;
  }
  .person-title {
    margin: 0;
    font-size: 22px;
    font-weight: 400;
    line-height: 26px;
  }
  .contact-list {
    list-style: none;
    margin: 33px 0 0;
    padding: 0;
  }
  .contact-item {
    display: flex;
    align-items: center;
    height: 33px;
    font-size: 24px;
  }
  .contact-icon {
    width: 26px;
    height: 26px;
    margin-right: 8px;
    flex: none;
  }
  .contact-icon circle { fill: none; stroke: var(--card-white); stroke-width: 1.8; }
  .contact-icon .glyph { fill: var(--card-white); }
  .contact-icon .glyph-line { fill: none; stroke: var(--card-white); stroke-width: 1.6; }

  .company-name {
    margin: 38px 0 0;
    font-size: 26px;
    font-weight: 700;
    line-height: 30px;
  }
  .address {
    margin: 14px 0 0;
    font-style: normal;
    font-size: 23px;
    line-height: 29.5px;
  }
  .abn {
    margin: 24px 0 0;
    font-size: 23px;
  }

  .brand {
    position: absolute;
    left: 470px;
    right: 0;
    top: 232px;
    display: flex;
    align-items: center;
    justify-content: center;
    gap: 16px;
  }
  .brand-square {
    width: 46px;
    height: 46px;
    background: var(--brand-blue);
  }
  .brand-name {
    font-size: 46px;
    font-weight: 700;
    color: var(--brand-blue);
    letter-spacing: 1px;
    line-height: 1;
  }
</style>
</head>
<body>
<div class="canvas">
  <section class="card">
    <svg class="card-shapes" width="940" height="536" viewBox="0 0 940 536" aria-hidden="true">
      <path class="shape-grey" d="M490,0 Q360,268 490,536 L486,536 Q376,268 486,0 Z"/>
      <path class="shape-blue" d="M0,0 H484 Q352,268 484,536 H0 Z"/>
    </svg>

    <div class="details">
      <h1 class="person-name">Derek Wallis</h1>
      <p class="person-title">Chief Operations Officer</p>

      <ul class="contact-list">
        <li class="contact-item">
          <svg class="contact-icon" viewBox="0 0 26 26" aria-hidden="true">
            <circle cx="13" cy="13" r="11.5"/>
            <path class="glyph" d="M6.5,11 Q13,6 19.5,11 L18,13 L16,12 L16,11 Q13,10 10,11 L10,12 L8,13 Z"/>
            <rect class="glyph" x="8.5" y="13.5" width="9" height="5" rx="1"/>
          </svg>
          02 7153 2819
        </li>
        <li class="contact-item">
          <svg class="contact-icon" viewBox="0 0 26 26" aria-hidden="true">
            <circle cx="13" cy="13" r="11.5"/>
            <rect class="glyph-line" x="9.5" y="6" width="7" height="14" rx="1.5"/>
            <circle class="glyph" cx="13" cy="17.5" r="0.9" style="stroke:none"/>
          </svg>
          0418 395 207
        </li>
        <li class="contact-item">
          <svg class="contact-icon" viewBox="0 0 26 26" aria-hidden="true">
            <circle cx="13" cy="13" r="11.5"/>
            <rect class="glyph" x="7" y="9" width="12" height="8" rx="1"/>
            <path d="M7.5,9.5 L13,14 L18.5,9.5" fill="none" stroke="#0255a3" stroke-width="1.2"/>
          </svg>
          derek@morvanetally.com
        </li>
      </ul>

      <h2 class="company-name">Morvane Tally Pty Ltd</h2>
      <address class="address">
        Level 22, Halden Court<br>
        48 Wirrapool St<br>
        Sydney NSW 2000
      </address>
      <p class="abn">ABN : 57 304 918 226</p>
    </div>

    <div class="brand">
      <span class="brand-square"></span>
      <span class="brand-name">MORVANE TALLY</span>
    </div>
  </section>
</div>
</body>
</html>
```